TBrandow executive consulting

We need a basic clean website for executive consulting. Rosalind is the previos CIO for bluecrest skyways and currently supports several technology companies with innovation and transformation.

Target Market(s)

C level technology and CIO training

Industry/Entity Type

Technology and travel industry

Coding

Coded - Design and coding required

Number of Pages Required

3 page

Font styles to use
Sans Serif

Colors
0054AA
0677BA
7BADD7
CADEEF
E8F1F8
0094D4
00A9DD
6FCCEA
C7EBF8
E9F6FB

Requirements
Must have
• Home page, about us, services social media links

```html
<!DOCTYPE html>
<html lang="en">
<head>
<meta charset="utf-8">
<title>TBrandow Executive Consulting</title>
<link href="https://fonts.googleapis.com/css2?family=Playfair+Display:wght@600;700&family=Poppins:wght@400;500;600;700&display=swap" rel="stylesheet">
<style>
:root{
  --blue-deep:#0054AA;
  --blue:#0677BA;
  --blue-mid:#7BADD7;
  --blue-pale:#CADEEF;
  --blue-mist:#E8F1F8;
  --sky:#0094D4;
  --sky-soft:#C7EBF8;
  --ink:#1f1f1f;
  --text:#3a3a3a;
  --grey-bg:#efefef;
  --footer:#222222;
  --white:#ffffff;
  --gold:#f5b400;
}
*{box-sizing:border-box;margin:0;padding:0}
html,body{width:1200px;height:3220px;overflow:hidden;background:var(--white)}
body{font-family:'Poppins',sans-serif;color:var(--text)}
.page{position:relative;width:1200px;height:3220px;overflow:hidden}
.abs{position:absolute}

/* header */
.site-header{position:absolute;left:0;top:0;width:1200px;height:100px;background:var(--white)}
.brand{position:absolute;left:88px;top:26px;font-family:'Playfair Display',serif;font-weight:700;font-size:34px;color:var(--ink);display:flex;align-items:center;gap:10px}
.brand-dot{width:14px;height:14px;border-radius:50%;background:var(--blue)}
.nav{position:absolute;top:44px;font-size:15px;font-weight:500;color:var(--ink);letter-spacing:.2px}
.nav.active{color:var(--blue);font-weight:600}
.nav-marker{position:absolute;left:669px;top:0;width:65px;height:4px;background:var(--blue)}
.btn-contact{position:absolute;left:982px;top:34px;width:128px;height:39px;border-radius:20px;background:var(--blue);color:var(--white);font-size:12.5px;font-weight:600;display:flex;align-items:center;justify-content:center}

/* hero */
.hero{position:absolute;left:0;top:100px;width:1200px;height:700px;background:linear-gradient(120deg,#0a5c8c 0%,#0b6fa6 45%,#0a4f7d 100%)}
.hero-arc{position:absolute;left:700px;top:100px;width:500px;height:700px}
.portrait{position:absolute;left:645px;top:100px;width:555px;height:700px;border-bottom-right-radius:260px;background:linear-gradient(180deg,#1c6e9b 0%,#2b5676 45%,#1b2736 100%)}
.hero-title{position:absolute;left:88px;top:326px;font-family:'Playfair Display',serif;font-weight:700;font-size:60px;line-height:63px;color:var(--white)}
.hero-copy{position:absolute;left:90px;top:474px;width:480px;font-size:16px;line-height:23px;color:var(--white)}
.btn{position:absolute;height:45px;border-radius:23px;font-size:14.5px;font-weight:600;display:flex;align-items:center;justify-content:center;letter-spacing:.2px}
.btn-dark{left:88px;top:570px;width:165px;background:#1e1e1e;color:var(--white)}
.btn-light{left:264px;top:570px;width:214px;background:var(--white);color:var(--ink)}
.scroll-down{position:absolute;left:952px;top:751px;width:102px;height:102px;border-radius:50%;background:var(--white);box-shadow:0 10px 30px rgba(0,0,0,.12);display:flex;align-items:center;justify-content:center}

.ring{position:absolute;border:1px solid #9a9a9a;border-radius:50%}

/* about */
.about-photo{position:absolute;left:96px;top:905px;width:465px;height:545px;border-radius:20px 110px 20px 110px;background:linear-gradient(135deg,#5d7e8e 0%,#31505f 50%,#a9b8bd 100%);box-shadow:0 18px 30px rgba(0,0,0,.18)}
.section-title{font-family:'Playfair Display',serif;font-weight:700;color:var(--ink)}
.about-title{position:absolute;left:617px;top:1010px;font-size:42px}
.about-copy{position:absolute;left:618px;top:1076px;width:482px;font-size:14.8px;line-height:21.2px;color:var(--text)}
.about-copy p+p{margin-top:10px}

/* stats */
.stat{position:absolute;top:1510px;width:240px;text-align:center;font-family:'Playfair Display',serif;color:var(--ink)}
.stat-num{font-size:62px;font-weight:700;line-height:80px;height:80px}
.stat-num small{font-size:34px;line-height:0}
.stat-label{font-size:19px;font-weight:600;line-height:26px;margin-top:-4px}
.stat.accent .stat-num{color:var(--blue)}

/* services */
.services{position:absolute;left:0;top:1678px;width:1200px;height:457px;background:var(--grey-bg)}
.services-title{position:absolute;left:0;top:1740px;width:1200px;text-align:center;font-size:42px}
.card{position:absolute;top:1818px;width:241px;height:178px;background:var(--white);border-radius:18px 18px 4px 4px;box-shadow:0 10px 20px rgba(0,0,0,.06)}
.card.featured{background:var(--blue);color:var(--white)}
.card-icon{position:absolute;left:24px;top:22px}
.card-title{position:absolute;left:95px;top:22px;width:112px;font-size:13px;line-height:17px;font-weight:600;color:var(--ink)}
.card.featured .card-title{color:var(--white)}
.card-rule{position:absolute;left:18px;right:18px;top:88px;height:1px;background:#dcdcdc}
.card.featured .card-rule{background:rgba(255,255,255,.5)}
.card-copy{position:absolute;left:24px;top:106px;width:200px;font-size:12px;line-height:17px;color:var(--text)}
.card.featured .card-copy{color:var(--white)}
.btn-outline{position:absolute;left:502px;top:2030px;width:195px;height:46px;border:1.5px solid #333;border-radius:23px;font-size:14px;font-weight:600;color:var(--ink);display:flex;align-items:center;justify-content:center;letter-spacing:.4px}

/* testimonials */
.testi-title{position:absolute;left:0;top:2203px;width:1200px;text-align:center;font-size:40px}
.testi{position:absolute;top:2288px;width:418px;height:224px;background:var(--white);border-radius:30px;box-shadow:0 12px 30px rgba(0,0,0,.07)}
.testi.active{border:1.5px solid var(--blue)}
.avatar{position:absolute;left:38px;top:30px;width:72px;height:72px;border-radius:50%;background:linear-gradient(180deg,#cfd9e2,#2d5c8c)}
.testi-name{position:absolute;left:121px;top:41px;font-size:16.5px;font-weight:600;color:var(--ink)}
.testi-name small{font-size:10px;font-weight:500}
.stars{position:absolute;left:121px;top:62px;font-size:18px;letter-spacing:1px;color:var(--gold)}
.stars span{color:#f3dfa5}
.quote-mark{position:absolute;right:22px;top:56px}
.testi-copy{position:absolute;left:33px;top:120px;width:350px;font-size:12.5px;line-height:19.5px;color:var(--text)}
.dot{position:absolute;top:2546px;width:12px;height:12px;border-radius:50%;background:#cfcfcf}
.dot.on{background:var(--blue)}

/* connect */
.watermark{position:absolute;left:0;top:2577px;width:1200px;text-align:center;font-family:'Playfair Display',serif;font-weight:700;font-size:110px;line-height:120px;color:var(--blue-mist);letter-spacing:2px;opacity:.8}
.connect-title{position:absolute;left:0;top:2632px;width:1200px;text-align:center;font-size:58px;line-height:80px}
.connect-copy{position:absolute;left:0;top:2711px;width:1200px;text-align:center;font-size:18px;line-height:26px;color:var(--text)}
.social{position:absolute;top:2756px;width:38px;height:38px;border-radius:50%}

/* footer */
.footer{position:absolute;left:0;top:2855px;width:1200px;height:365px;background:var(--footer)}
.footer-brand{position:absolute;left:145px;top:2930px;font-family:'Playfair Display',serif;font-weight:700;font-size:40px;color:var(--white);display:flex;align-items:center;gap:10px}
.footer-brand .brand-dot{background:var(--white)}
.footer-note{position:absolute;left:145px;top:3008px;width:290px;font-size:14px;line-height:19px;color:var(--white)}
.subscribe{position:absolute;left:145px;top:3063px;width:273px;height:48px;border-radius:24px;background:var(--white);font-size:12.5px;color:#666;padding-left:27px;display:flex;align-items:center}
.subscribe svg{position:absolute;right:14px;top:14px}
.f-head{position:absolute;top:2925px;font-family:'Playfair Display',serif;font-weight:600;font-size:18px;color:var(--white)}
.f-link{position:absolute;font-size:14px;color:var(--white)}
.f-label{position:absolute;font-size:12px;font-weight:600;color:var(--white)}
.f-val{position:absolute;font-size:12.5px;line-height:17px;color:var(--white)}
.f-icon{position:absolute;left:944px;width:26px;height:26px;border-radius:50%;background:#3a3a3a}
.footer-rule{position:absolute;left:78px;top:3182px;width:1044px;height:1px;background:#4a4a4a}
.copyright{position:absolute;left:0;top:3196px;width:1200px;text-align:center;font-size:11px;font-weight:500;color:var(--white)}
.chat{position:absolute;left:1129px;top:3154px;width:52px;height:52px;border-radius:50%;background:var(--sky);display:flex;align-items:center;justify-content:center}
</style>
</head>
<body>
<div class="page">

  <header class="site-header">
    <div class="brand"><span class="brand-dot"></span>TBrandow</div>
    <div class="nav-marker"></div>
    <div class="nav active" style="left:679px">HOME</div>
    <div class="nav" style="left:760px">ABOUT US</div>
    <div class="nav" style="left:874px">SERVICES</div>
    <div class="btn-contact">CONTACT US</div>
  </header>

  <section class="hero" role="img" aria-label="Blue-toned city skyline with digital technology overlay"></section>
  <svg class="hero-arc" viewBox="0 0 500 700" aria-hidden="true">
    <path d="M500 420 C500 620 420 700 250 700 L500 700 Z" fill="#e6e8f3"/>
  </svg>
  <div class="portrait" role="img" aria-label="Portrait of Rosalind Brandow smiling, wearing a dark blazer"></div>
  <h1 class="hero-title">Innovating the<br>Future of Technology</h1>
  <p class="hero-copy">Rosalind Brandow, former Chief Information Officer of Bluecrest Skyways, now supports several technology companies with innovation and transformation.</p>
  <div class="btn btn-dark">GET IN TOUCH</div>
  <div class="btn btn-light">ABOUT OUR COMPANY</div>
  <div class="scroll-down">
    <svg width="22" height="28" viewBox="0 0 22 28"><path d="M11 2 V25 M3 17 L11 25 L19 17" fill="none" stroke="#0677BA" stroke-width="2"/></svg>
  </div>

  <div class="ring" style="left:1086px;top:828px;width:230px;height:230px"></div>
  <div class="ring" style="left:-98px;top:993px;width:180px;height:225px"></div>
  <div class="ring" style="left:1063px;top:2058px;width:270px;height:270px"></div>
  <div class="ring" style="left:-140px;top:2335px;width:258px;height:304px"></div>
  <div class="ring" style="left:1000px;top:2526px;width:68px;height:68px"></div>

  <div class="about-photo" role="img" aria-label="Two professionals working at a laptop with digital infographic overlay"></div>
  <div class="ring" style="left:528px;top:1416px;width:60px;height:60px"></div>
  <h2 class="section-title about-title">About Rosalind Brandow</h2>
  <div class="about-copy">
    <p>Rosalind Brandow is a seasoned leader with a remarkable 40-year career in the travel industry, including 20 transformative years at Bluecrest Skyways. As the Senior Vice President of Technology (CIO), Rosalind spearheaded some of the company’s most significant technological and strategic transformations, helping Bluecrest Skyways stay at the forefront of innovation in the competitive travel market. Her work bridged the gap between business strategy and technology, driving measurable success and resilience.</p>
    <p>With expertise in Leadership, Mentorship, Technology Strategy, and Digital Transformation, Rosalind is passionate about empowering IT leaders to forge stronger connections between their technology teams and business goals. Her approach is rooted in a belief that technology is not just a tool but a catalyst for growth, collaboration, and innovation.</p>
  </div>

  <div class="stat" style="left:93px"><div class="stat-num">200+</div><div class="stat-label">Companies helped</div></div>
  <div class="stat accent" style="left:349px"><div class="stat-num">150<small>M</small></div><div class="stat-label">Revenue generated</div></div>
  <div class="stat" style="left:606px"><div class="stat-num">200+</div><div class="stat-label">Companies helped</div></div>
  <div class="stat" style="left:862px"><div class="stat-num">150<small>M</small></div><div class="stat-label">Revenue generated</div></div>

  <section class="services" role="img" aria-label="Light grey background with faint network pattern"></section>
  <svg class="abs" style="left:0;top:1678px" width="170" height="150" viewBox="0 0 170 150" aria-hidden="true">
    <path d="M0 150 C0 60 60 0 160 0 L0 0 Z" fill="#d6ebf4"/>
  </svg>
  <h2 class="section-title services-title">Our Services</h2>

  <div class="card" style="left:100px">
    <svg class="card-icon" width="56" height="56" viewBox="0 0 56 56"><circle cx="28" cy="24" r="14" fill="none" stroke="#0677BA" stroke-width="2"/><circle cx="28" cy="24" r="6" fill="none" stroke="#0677BA" stroke-width="2"/><path d="M6 30 Q8 48 22 50 M50 30 Q48 48 34 50" fill="none" stroke="#0677BA" stroke-width="2"/></svg>
    <div class="card-title">Organizational Change Management</div>
    <div class="card-rule"></div>
    <div class="card-copy">Guiding companies through large-scale IT and organizational changes.</div>
  </div>
  <div class="card" style="left:354px">
    <svg class="card-icon" width="56" height="56" viewBox="0 0 56 56"><circle cx="28" cy="28" r="9" fill="none" stroke="#0677BA" stroke-width="2"/><path d="M28 8 V16 M28 40 V48 M8 28 H16 M40 28 H48 M14 14 L20 20 M42 14 L36 20 M14 42 L20 36 M42 42 L36 36" stroke="#0677BA" stroke-width="2"/></svg>
    <div class="card-title">Technology Strategy Development</div>
    <div class="card-rule"></div>
    <div class="card-copy">Aligning IT strategies with business goals for growth and innovation.</div>
  </div>
  <div class="card featured" style="left:608px">
    <svg class="card-icon" width="56" height="56" viewBox="0 0 56 56"><circle cx="28" cy="28" r="13" fill="none" stroke="#fff" stroke-width="2"/><path d="M15 28 H41 M28 15 V41" stroke="#fff" stroke-width="2"/><circle cx="8" cy="28" r="3" fill="none" stroke="#fff" stroke-width="2"/><circle cx="48" cy="28" r="3" fill="none" stroke="#fff" stroke-width="2"/><circle cx="28" cy="7" r="3" fill="none" stroke="#fff" stroke-width="2"/><circle cx="28" cy="49" r="3" fill="none" stroke="#fff" stroke-width="2"/></svg>
    <div class="card-title">Digital Transformation Consulting</div>
    <div class="card-rule"></div>
    <div class="card-copy">Executive coaching for IT leaders to enhance strategic decision -making and leadership skills.</div>
  </div>
  <div class="card" style="left:862px">
    <svg class="card-icon" width="56" height="56" viewBox="0 0 56 56"><circle cx="28" cy="16" r="9" fill="none" stroke="#0677BA" stroke-width="2"/><path d="M6 36 L18 30 L28 38 L38 30 L50 36 M14 40 L24 48 M22 38 L32 46" fill="none" stroke="#0677BA" stroke-width="2"/></svg>
    <div class="card-title">T-Business Partnership Development</div>
    <div class="card-rule"></div>
    <div class="card-copy">Strengthening collaboration between IT and business units for seamless decision-making.</div>
  </div>
  <div class="btn-outline">VIEW ALL SERVICES</div>

  <h2 class="section-title testi-title">Client Testimonials</h2>
  <div class="testi" style="left:170px">
    <div class="avatar" role="img" aria-label="Client headshot"></div>
    <div class="testi-name">Northfield Canopy</div>
    <div class="stars">★★★★<span>★</span></div>
    <svg class="quote-mark" width="80" height="44" viewBox="0 0 80 44"><path d="M22 0 H38 L20 44 H4 Z M60 0 H76 L58 44 H42 Z" fill="#ececec"/></svg>
    <p class="testi-copy">Rosalind is a decisive and fair leader who exemplifies strength, wisdom, and empathy. She always possesses a clear vision for the future and is willing to make bold decisions which are grounded...</p>
  </div>
  <div class="testi active" style="left:614px">
    <div class="avatar" role="img" aria-label="Client headshot"></div>
    <div class="testi-name">Martin Ellery, <small>CEO Q4NX</small></div>
    <div class="stars">★★★★<span>★</span></div>
    <svg class="quote-mark" width="80" height="44" viewBox="0 0 80 44"><path d="M22 0 H38 L20 44 H4 Z M60 0 H76 L58 44 H42 Z" fill="#ececec"/></svg>
    <p class="testi-copy">Rosalind is a decisive and fair leader who exemplifies strength, wisdom, and empathy. She always possesses a clear vision for the future and is willing to make bold decisions which are grounded...</p>
  </div>
  <div class="dot on" style="left:571px"></div>
  <div class="dot" style="left:591px"></div>
  <div class="dot" style="left:611px"></div>

  <div class="watermark">SOCIAL MEDIA</div>
  <h2 class="section-title connect-title">Connect With Rosalind</h2>
  <p class="connect-copy">Ready to elevate your IT strategy? Let’s discuss how TBrandow Consulting can help.</p>
  <div class="social" style="left:509px;background:#3b5aa0" aria-label="Circlefeed"></div>
  <div class="social" style="left:554px;background:#1da1e2" aria-label="Chirpline"></div>
  <div class="social" style="left:599px;background:#e0242b" aria-label="Searchly"></div>
  <div class="social" style="left:644px;background:#0d3d6e" aria-label="Worknet"></div>

  <footer class="footer"></footer>
  <svg class="abs" style="left:1000px;top:2855px" width="200" height="200" viewBox="0 0 200 200" aria-hidden="true">
    <path d="M0 0 H200 V200 C200 90 130 0 40 0 Z" fill="#ffffff"/>
    <path d="M40 0 C130 0 200 90 200 200 V150 C185 70 130 10 70 0 Z" fill="#d6ebf4"/>
  </svg>
  <div class="footer-brand"><span class="brand-dot"></span>TBrandow</div>
  <p class="footer-note">Subscribe to our news letter to get the latest news.</p>
  <div class="subscribe">Enter email address
    <svg width="20" height="20" viewBox="0 0 20 20"><path d="M1 9 L19 1 L14 19 L9 12 Z M9 12 L19 1" fill="#0054AA" stroke="#0054AA" stroke-width="1"/></svg>
  </div>

  <div class="f-head" style="left:505px">Quick links</div>
  <div class="f-link" style="left:505px;top:2967px">Home</div>
  <div class="f-link" style="left:505px;top:3003px">About us</div>
  <div class="f-link" style="left:505px;top:3038px">services</div>
  <div class="f-link" style="left:505px;top:3074px">Contact us</div>

  <div class="f-head" style="left:686px">Contact Info</div>
  <svg class="abs" style="left:686px;top:2965px" width="14" height="14" viewBox="0 0 14 14"><path d="M2 1 L5 1 L6 4 L4 5.5 Q6 9 8.5 10 L10 8 L13 9 L13 12 Q7 13 3.5 9 Q0 5 2 1 Z" fill="#0094D4"/></svg>
  <div class="f-label" style="left:708px;top:2967px">PHONE</div>
  <div class="f-val" style="left:708px;top:2983px">+044-555-0142</div>
  <svg class="abs" style="left:686px;top:3014px" width="14" height="11" viewBox="0 0 14 11"><rect width="14" height="11" rx="1" fill="#0094D4"/><path d="M1 1 L7 6 L13 1" fill="none" stroke="#222" stroke-width="1.2"/></svg>
  <div class="f-label" style="left:708px;top:3013px">EMAIL</div>
  <div class="f-val" style="left:708px;top:3029px">hello@tbrandow-consult.net</div>
  <svg class="abs" style="left:687px;top:3081px" width="12" height="16" viewBox="0 0 12 16"><path d="M6 0 C2.7 0 0 2.6 0 6 C0 10 6 16 6 16 C6 16 12 10 12 6 C12 2.6 9.3 0 6 0 Z" fill="#0094D4"/><circle cx="6" cy="6" r="2.2" fill="#222"/></svg>
  <div class="f-label" style="left:708px;top:3076px">ADDRESS</div>
  <div class="f-val" style="left:708px;top:3092px">Some Address line here<br>united kingdom ZX9 4QP</div>

  <div class="f-head" style="left:944px">Folow Us</div>
  <div class="f-icon" style="top:2972px"></div><div class="f-link" style="left:982px;top:2976px">Circlefeed</div>
  <div class="f-icon" style="top:3006px"></div><div class="f-link" style="left:982px;top:3010px">Chirpline</div>
  <div class="f-icon" style="top:3040px"></div><div class="f-link" style="left:982px;top:3044px">Searchly</div>
  <div class="f-icon" style="top:3074px"></div><div class="f-link" style="left:982px;top:3078px">Worknet</div>

  <div class="footer-rule"></div>
  <div class="copyright">© COPYRIGHT 2025 ROSALIND BRANDOW, ALL RIGHTS RESERVED</div>
  <div class="chat">
    <svg width="30" height="26" viewBox="0 0 30 26"><path d="M15 2 C7 2 2 7 2 12 C2 15 4 18 7 19.5 L6 24 L11 21 C12 21.3 13.5 21.5 15 21.5 C23 21.5 28 17 28 12 C28 7 23 2 15 2 Z" fill="#fff"/><circle cx="10" cy="12" r="1.6" fill="#0094D4"/><circle cx="15" cy="12" r="1.6" fill="#0094D4"/><circle cx="20" cy="12" r="1.6" fill="#0094D4"/></svg>
  </div>

</div>
</body>
</html>
```